A stationary and business card desgn for a podiatry clinic

i require a stationary design for letter heads, envelopes, buisness cards.

it is for a new podiatry practise within a medical centre, that deals with all lower limb pathology and injury and foot related problems.

the colour scheme for my exisiting logo is orange blue and white. colours provided below.
i would like a white background for the buisness card.

the final design should portray health and wellbeing in a professional manner that still looks modern but sophisticated.

male and female, off all ethinical backgrounds aged between 30-80 years

Medical

• letter head.
need to include all contact details mentioned below.
need to also include ABN 53120978446

i prefer the logo on the top left hand corner and the contact info on the right. the address can be written in a sentence like form as the footer.

Business card
Front:

include logo provided.

clinic details on the front of the card.

Delphine Carrow
B.Pod

P: 7394 5186
F: 7394 5130
M: 0437 612 908
E: delphine@tavrin.com.au
W: www.tavrin.com.au

(may use icons to indicate contact type)

on back

Appointments:

lines to write dates, time etc.
(3-4 of these)
and a small photo of just the foot from the logo in coloured watermark.

Address:
Brackwell Medical Centre
47 Tallowin Street
Brackwell SA 5174
(this location infomation could be in smaller font at the bottom of the buisness card under a line, running in a sentence like fashion) or in the bottom left or right hand corner in a paragraph like you would write it on an envelope

however if you think a different lay out at the back will look better by all means i just need to have room for the appointment even if it is just lines/ space.

i also prefer square cards not rounded corners.

thanks
• plain texts such as times new roman and arial

```html
<!DOCTYPE html>
<html lang="en">
<head>
<meta charset="utf-8">
<title>Tavrin Podiatry – Stationery</title>
<link rel="stylesheet" href="https://fonts.googleapis.com/css2?family=Arimo:wght@400;700&family=Open+Sans:wght@400;600&family=Questrial&display=swap">
<style>
  :root {
    --orange: #e8601c;
    --blue: #2e3a8c;
    --orange-soft: #f6c9ae;
    --ink: #2b2b2b;
    --paper: #ffffff;
    --backdrop: #ebebeb;
  }
  * { margin: 0; padding: 0; box-sizing: border-box; }
  html, body { width: 1200px; height: 900px; overflow: hidden; }
  body { background: var(--backdrop); position: relative; font-family: "Arimo", Arial, sans-serif; color: var(--ink); }

  .sheet { position: absolute; background: var(--paper); box-shadow: 2px 3px 6px rgba(0,0,0,.18); }

  .brand-name {
    font-family: "Open Sans", Arial, sans-serif;
    font-weight: 600;
    color: var(--blue);
    display: flex; align-items: center; gap: 7px;
    white-space: nowrap;
  }
  .brand-dot { width: 12px; height: 12px; border-radius: 50%; background: var(--orange); flex: none; }

  .address-band {
    position: absolute; left: 0; right: 0; bottom: 0;
    background: var(--orange); color: #fff;
    font-family: "Questrial", Arial, sans-serif;
    display: flex; align-items: center; justify-content: center;
    white-space: nowrap;
  }

  .contact-list { list-style: none; font-family: "Questrial", Arial, sans-serif; }
  .contact-list li { display: flex; align-items: center; gap: 6px; white-space: nowrap; }
  .contact-list svg { flex: none; fill: var(--blue); }

  .divider { position: absolute; width: 2px; background: linear-gradient(var(--blue) 50%, var(--orange) 50%); }

  /* Business cards sit in front of the letterhead */
  .card-front, .card-back { z-index: 2; }

  /* Business card front */
  .card-front { left: 138px; top: 268px; width: 425px; height: 235px; }
  .card-front .brand-name { position: absolute; left: 20px; top: 98px; font-size: 18px; }
  .card-front .divider { left: 195px; top: 76px; height: 100px; }
  .holder { position: absolute; left: 218px; top: 35px; font-family: "Open Sans", Arial, sans-serif; }
  .holder-name { font-size: 18px; font-weight: 600; color: #333; }
  .holder-title { font-size: 18px; font-weight: 400; color: #444; margin-top: 2px; }
  .card-front .contact-list { position: absolute; left: 216px; top: 100px; font-size: 13.5px; line-height: 16.2px; color: #333; }
  .card-front .address-band, .card-back .address-band { height: 40px; font-size: 12.5px; }

  /* Business card back */
  .card-back { left: 138px; top: 577px; width: 425px; height: 236px; overflow: hidden; }
  .faint-mark { position: absolute; left: 290px; top: 30px; width: 110px; height: 110px; border-radius: 50%; background: var(--orange-soft); opacity: .6; }
  .appointments { position: absolute; left: 49px; top: 22px; font-family: "Questrial", Arial, sans-serif; font-size: 18px; color: #333; }
  .appointment-row { display: flex; align-items: baseline; height: 35px; white-space: nowrap; }
  .appointment-row span { display: inline-block; border-bottom: 1px solid #333; height: 1px; margin: 0 6px 0 2px; }
  .line-date { width: 58px; }
  .line-day { width: 60px; }
  .line-time { width: 60px; }

  /* Letterhead */
  .letterhead { left: 541px; top: 62px; width: 571px; height: 805px; z-index: 1; }
  .top-band { position: absolute; left: 0; right: 0; top: 0; height: 13px; background: var(--orange); }
  .letterhead .brand-name { position: absolute; left: 81px; top: 63px; font-size: 17px; }
  .letterhead .brand-dot { width: 10px; height: 10px; }
  .letterhead .divider { left: 371px; top: 57px; height: 47px; width: 1.5px; }
  .letterhead .contact-list { position: absolute; left: 388px; top: 56px; font-size: 8.5px; line-height: 9.6px; color: var(--blue); }
  .letter-body { position: absolute; left: 54px; top: 170px; width: 474px; font-size: 11.4px; line-height: 13.4px; color: #222; }
  .letter-body p { margin-bottom: 13.4px; }
  .letterhead .address-band { height: 24px; font-size: 9.5px; letter-spacing: 2px; }
</style>
</head>
<body>

<section class="sheet letterhead">
  <div class="top-band"></div>
  <div class="brand-name"><span class="brand-dot"></span>Tavrin Podiatry</div>
  <div class="divider"></div>
  <ul class="contact-list">
    <li><svg width="6" height="6" viewBox="0 0 10 10"><path d="M2 0h2l1 3-1.5 1a6 6 0 0 0 2.5 2.5L7 5l3 1v2c0 1-1 2-2 2A8 8 0 0 1 0 2c0-1 1-2 2-2z"/></svg>7394 5186</li>
    <li><svg width="6" height="6" viewBox="0 0 10 10"><rect x="0" y="3" width="10" height="5" rx="1"/></svg>7394 5130</li>
    <li><svg width="6" height="6" viewBox="0 0 10 10"><rect x="2.5" y="0" width="5" height="10" rx="1"/></svg>0437 612 908</li>
    <li><svg width="6" height="6" viewBox="0 0 10 10"><path d="M0 2h10v6H0z"/></svg>delphine@tavrin.com.au</li>
    <li><svg width="6" height="6" viewBox="0 0 10 10"><circle cx="5" cy="5" r="5"/></svg>www.tavrin.com.au</li>
  </ul>

  <div class="letter-body">
    <p>Dear Someone Somebody,</p>
    <p>Lorem ipsum dolor sit amet, consectetuer adipiscing elit. Praesent mattis eros a tellus. Quisque leo tortor, commodo id, dapibus et, lacinia et, justo. Ut urna sapien, dictum eu, cursus vel, consectetuer tincidunt, eros. Etiam in libero. Etiam tempor. Maecenas ligula felis, commodo eget, scelerisque id, suscipit nec, odio. Vivamus commodo, magna in mollis feugiat, felis nisl dapibus dolor, eu blandit orci nulla in orci. Cras felis ipsum, mollis at, semper et, tincidunt id, ipsum. Ut consectetuer elit nec elit. Cras luctus molestie ligula. In gravida tempor nunc.</p>
    <p>Curabitur nisl ligula, pulvinar et, volutpat non, porta a, ipsum. Donec tristique ante at est. Pellentesque volutpat est non diam. Aenean vel velit. Suspendisse facilisis nisl et massa. Mauris nec erat. Pellentesque luctus arcu ut dui. Proin suscipit lorem id augue. Maecenas eget ipsum nec orci convallis viverra. Suspendisse potenti. Donec sed enim. Ut et turpis. Ut mattis enim nec nisl. Ut quam. Pellentesque lobortis vehicula risus.</p>
    <p>Etiam massa erat, tempor et, elementum fringilla, pellentesque ac, odio. Cras sed felis. Aliquam erat volutpat. Etiam tristique. Donec pellentesque, nulla semper adipiscing faucibus, nibh augue semper sapien, eget feugiat dui massa et urna. Nullam ac arcu. Quisque interdum. Morbi tristique sagittis arcu. Phasellus euismod ante eget risus. Nam convallis rutrum augue. Pellentesque placerat ultrices tellus.</p>
    <p>Ut lacinia. Sed aliquet diam at odio. Nunc ultrices pretium urna. Sed risus velit, nonummy eget, suscipit at, sagittis in, tortor. Quisque risus. Duis porta. Nunc blandit, augue et nonummy ultrices, lacus justo tincidunt nibh, eu vestibulum turpis metus iaculis ipsum. Morbi neque. Quisque augue. Etiam eleifend rhoncus metus. Aliquam auctor libero non nisi.</p>
    <p>Pellentesque habitant morbi tristique senectus et netus et malesuada fames ac turpis egestas. Nullam justo lectus, lobortis id, pharetra eu, pulvinar ac, nibh. Sed hendrerit pretium urna. Vivamus ut ipsum eget justo adipiscing adipiscing. Donec lectus arcu, interdum eget, malesuada a, euismod sed, sapien. Proin imperdiet, nulla sit amet mattis adipiscing, enim nibh condimentum metus, sit amet lacinia tortor arcu eget magna. Mauris eget enim at ante luctus ultricies. Integer eu nunc eget tellus iaculis vestibulum. Suspendisse potenti. Aenean aliquam mauris id turpis.</p>
    <p>Your Sincerely,<br>Marcus Elton.</p>
  </div>

  <div class="address-band">Brackwell Medical Centre &nbsp;●&nbsp; 47 Tallowin Street &nbsp;●&nbsp; Brackwell SA 5174</div>
</section>

<section class="sheet card-front">
  <div class="brand-name"><span class="brand-dot"></span>Tavrin Podiatry</div>
  <div class="divider"></div>
  <div class="holder">
    <div class="holder-name">Delphine Carrow</div>
    <div class="holder-title">B.Pod</div>
  </div>
  <ul class="contact-list">
    <li><svg width="9" height="9" viewBox="0 0 10 10"><path d="M2 0h2l1 3-1.5 1a6 6 0 0 0 2.5 2.5L7 5l3 1v2c0 1-1 2-2 2A8 8 0 0 1 0 2c0-1 1-2 2-2z"/></svg>7394 5186</li>
    <li><svg width="9" height="9" viewBox="0 0 10 10"><rect x="2" y="0" width="6" height="3"/><rect x="0" y="3" width="10" height="5" rx="1"/><rect x="2" y="7" width="6" height="3"/></svg>7394 5130</li>
    <li><svg width="9" height="9" viewBox="0 0 10 10"><rect x="2.5" y="0" width="5" height="10" rx="1"/></svg>0437 612 908</li>
    <li><svg width="9" height="9" viewBox="0 0 10 10"><path d="M0 2h10v6H0z"/></svg>delphine@tavrin.com.au</li>
    <li><svg width="9" height="9" viewBox="0 0 10 10"><circle cx="5" cy="5" r="5"/></svg>www.tavrin.com.au</li>
  </ul>
  <div class="address-band">Brackwell Medical Centre ● 47 Tallowin Street ● Brackwell SA 5174</div>
</section>

<section class="sheet card-back">
  <div class="faint-mark"></div>
  <div class="appointments">
    <div class="appointment-row">Date:<span class="line-date"></span>Day:<span class="line-day"></span>Time:<span class="line-time"></span></div>
    <div class="appointment-row">Date:<span class="line-date"></span>Day:<span class="line-day"></span>Time:<span class="line-time"></span></div>
    <div class="appointment-row">Date:<span class="line-date"></span>Day:<span class="line-day"></span>Time:<span class="line-time"></span></div>
    <div class="appointment-row">Date:<span class="line-date"></span>Day:<span class="line-day"></span>Time:<span class="line-time"></span></div>
    <div class="appointment-row">Date:<span class="line-date"></span>Day:<span class="line-day"></span>Time:<span class="line-time"></span></div>
  </div>
  <div class="address-band">Brackwell Medical Centre ● 47 Tallowin Street ● Brackwell SA 5174</div>
</section>

</body>
</html>
```